Property risk and finance brokerage company needs a business card design

Tarlow Financial requires a business card design. Please integrate existing logo (refer uploaded file).
hex codes used on logo #002649 #008ED6 #444F51 #ADAFAA
font used - Cinzel
Contact information
Renata Sollisford
Director
Mobile: 0491 738 205
email: r.sollisford@tarlowfinancial.example.au
website: www.tarlowfinancial.example.au
CRN : 918354
PO Box 527
Canterbury, Victoria, 3126
Horizontal orientation please
Finance

```html
<!DOCTYPE html>
<html lang="en">
<head>
<meta charset="utf-8">
<title>Tarlow Financial – Business Card</title>
<link rel="stylesheet" href="https://fonts.googleapis.com/css2?family=Cinzel:wght@400&family=Open+Sans:wght@400;700&display=swap">
<style>
  :root {
    --navy: #002649;
    --blue: #008ED6;
    --slate: #444F51;
    --stone: #ADAFAA;
    --ink: #2b2f31;
    --paper: #ffffff;
    --backdrop: #e9eaee;
  }
  html, body {
    margin: 0;
    width: 1200px;
    height: 987px;
    overflow: hidden;
    background: var(--backdrop);
    font-family: "Open Sans", Arial, sans-serif;
  }
  .canvas { position: relative; width: 1200px; height: 987px; }
  .card {
    position: absolute;
    width: 620px;
    height: 360px;
    background: var(--paper);
    border-radius: 22px;
    box-shadow: 0 10px 28px rgba(40, 50, 70, 0.18);
    overflow: hidden;
  }
  .card--back { left: 520px; top: 70px; }
  .card--front { left: 60px; top: 520px; }

  /* brand name set as text */
  .brand {
    display: flex;
    align-items: center;
    gap: 12px;
    font-family: "Cinzel", Georgia, serif;
    font-weight: 400;
    color: var(--navy);
    white-space: nowrap;
  }
  .brand__dot {
    border-radius: 50%;
    background: var(--blue);
    flex: none;
  }

  /* back */
  .card--back .brand {
    position: absolute;
    left: 0; right: 0; top: 130px;
    justify-content: center;
    font-size: 34px;
  }
  .card--back .brand__dot { width: 26px; height: 26px; }
  .back__url {
    position: absolute;
    left: 0; right: 0; bottom: 62px;
    text-align: center;
    font-size: 19px;
    letter-spacing: 2px;
    color: var(--slate);
  }

  /* front */
  .card--front .brand {
    position: absolute;
    left: 34px; top: 150px;
    font-size: 25px;
  }
  .card--front .brand__dot { width: 20px; height: 20px; }
  .divider {
    position: absolute;
    left: 318px; top: 50px;
    width: 2px; height: 260px;
    background: linear-gradient(to bottom, rgba(173,175,170,0), var(--stone) 40%, rgba(173,175,170,0));
  }
  .contact {
    position: absolute;
    left: 342px; top: 56px;
    color: var(--ink);
  }
  .contact__name {
    margin: 0;
    font-size: 24px;
    font-weight: 700;
    color: var(--navy);
    line-height: 1.1;
  }
  .contact__title {
    margin: 2px 0 14px;
    font-size: 15px;
    color: var(--slate);
  }
  .contact__list { list-style: none; margin: 0; padding: 0; }
  .contact__item {
    display: flex;
    align-items: center;
    gap: 8px;
    font-size: 15px;
    line-height: 25px;
    white-space: nowrap;
  }
  .contact__icon { width: 15px; height: 15px; flex: none; fill: var(--navy); }
  .contact__address {
    margin: 14px 0 0;
    font-size: 15px;
    line-height: 21px;
    color: var(--ink);
  }
</style>
</head>
<body>
<main class="canvas">

  <section class="card card--back" aria-label="Card back">
    <div class="brand"><span class="brand__dot"></span>Tarlow Financial</div>
    <p class="back__url">www.tarlowfinancial.example.au</p>
  </section>

  <section class="card card--front" aria-label="Card front">
    <div class="brand"><span class="brand__dot"></span>Tarlow Financial</div>
    <div class="divider"></div>

    <div class="contact">
      <p class="contact__name">Your Name</p>
      <p class="contact__title">Title</p>
      <ul class="contact__list">
        <li class="contact__item">
          <svg class="contact__icon" viewBox="0 0 16 16" aria-hidden="true"><path d="M3.5 1 6 3.6 4.7 5.4c.9 2.2 2.6 4 4.9 5l1.8-1.3L14 11.6 12.4 14C7 14 2 9 2 3.6z"/></svg>
          012-345-6789
        </li>
        <li class="contact__item">
          <svg class="contact__icon" viewBox="0 0 16 16" aria-hidden="true"><rect x="4" y="1" width="8" height="4"/><rect x="1" y="6" width="14" height="6" rx="1"/><rect x="4" y="10" width="8" height="5" fill="#fff" stroke="#002649"/></svg>
          012-345-6789
        </li>
        <li class="contact__item">
          <svg class="contact__icon" viewBox="0 0 16 16" aria-hidden="true"><rect x="1" y="3" width="14" height="10" rx="1"/><path d="M1.5 3.5 8 9l6.5-5.5" stroke="#fff" stroke-width="1.4" fill="none"/></svg>
          info@tarlowfinancial.example.au
        </li>
        <li class="contact__item">
          <svg class="contact__icon" viewBox="0 0 16 16" aria-hidden="true"><circle cx="8" cy="8" r="7"/><path d="M1 8h14M8 1c-3 3.5-3 10.5 0 14M8 1c3 3.5 3 10.5 0 14" stroke="#fff" fill="none"/></svg>
          www.tarlowfinancial.example.au
        </li>
      </ul>
      <p class="contact__address">Street Name, City Name<br>Zip Code-00000</p>
    </div>
  </section>

</main>
</body>
</html>
```